Redesign (8 documents) attached with brand guidelines - very quick/easy job!

We have 8 flyers/documents that we need put into the style of our new brand (see attached). So this is a simple rebrand exercise - complete with our brand guidelines (see attached)

I would need the designer to sign an NDA prior to taking this piece of work as I will be sharing newly branded documents with you prior to market release.

If these are done well we would as the same designer to work on a z-card designed brochure/POS

Brief:

- These are documents that customers would need to complete in order to book a particular service
- If you use images (ideally from Pixvane, so we don’t have to pay for them!)
- Icon ideas enclosed
-All the content on the brochures is required: but if you think it would 'flow better' in a different order that is fine.

Target Market(s)

Customers interested in receiving a particular service

Industry/Entity Type

Work

Other font styles liked:
• Brandon (see brand guide)

Requirements
Must have
• A4
Nice to have
• New logo ideas
Should not have
• Anything out of brand guidleines

```html
<!DOCTYPE html>
<html lang="en">
<head>
<meta charset="utf-8">
<title>Nutritional Therapy Consultation Report</title>
<link href="https://fonts.googleapis.com/css2?family=Mulish:wght@400;600;700&display=swap" rel="stylesheet">
<style>
:root{
  --teal:#1a9fc4;
  --teal-dark:#1689ab;
  --yellow:#efe32a;
  --pill-grey:#b4b4b4;
  --head-grey:#a9a9a9;
  --rule:#c9c9c9;
  --rule-teal:#7ecbe0;
  --ink:#555;
  --backdrop:#ecebe8;
  --paper:#ffffff;
}
*{box-sizing:border-box;margin:0;padding:0}
html,body{width:1200px;height:900px;overflow:hidden}
body{background:var(--backdrop);font-family:"Mulish",Arial,sans-serif;color:var(--ink);position:relative}
.page{position:absolute;top:67px;width:535px;height:761px;background:var(--paper);box-shadow:0 2px 8px rgba(0,0,0,.15)}
.page--one{left:60px}
.page--two{left:610px}
.abs{position:absolute}
.brand-tab{left:0;top:37px;width:183px;height:64px;background:var(--teal);border-radius:0 32px 32px 0;display:flex;align-items:center;padding-left:38px}
.brand-name{color:var(--yellow);font-weight:700;font-size:19px;letter-spacing:.5px}
.doc-title{left:201px;top:60px;color:var(--teal);font-size:12.5px;font-weight:600;line-height:15px;letter-spacing:.3px}
.field{width:218px;height:18px;border-bottom:1px solid var(--rule-teal);font-size:9px;font-weight:600;color:#444;padding-top:3px}
.pill{height:22px;width:217px;border-radius:11px;font-size:8.5px;font-weight:600;display:flex;align-items:center;padding-left:11px;letter-spacing:.2px;color:#fff;text-transform:uppercase}
.pill--grey{background:var(--pill-grey)}
.pill--teal{background:var(--teal)}
.pill--accent{color:var(--yellow)}
.ruled{background-image:repeating-linear-gradient(to bottom,transparent 0 17px,var(--rule) 17px 18px)}
.ruled--teal{background-image:repeating-linear-gradient(to bottom,transparent 0 17px,var(--rule-teal) 17px 18px)}
.notes{left:38px;width:457px;height:90px}
.table{left:38px;width:457px;display:flex;gap:3px}
.col{flex:1}
.col-head{height:21px;background:var(--head-grey);color:#fff;font-size:8.5px;padding:3px 9px 0;line-height:9.5px;display:flex;align-items:flex-start}
.col-head--single{align-items:center;padding-top:0}
.col-body{height:110px;margin-top:-1px;background-position:0 11px}
.icon{left:465px;width:30px;height:30px;background:var(--teal)}
.icon svg{display:block}
.photo{border-radius:0}
.photo--nuts{left:38px;top:0;width:148px;height:110px;background:linear-gradient(135deg,#8a6a48,#c9a46b 55%,#5d4430)}
.photo--asparagus{left:198px;top:22px;width:140px;height:88px;background:linear-gradient(135deg,#6f8a3e,#a6b86a 50%,#6b5236)}
.photo--carrots{left:349px;top:0;width:145px;height:131px;background:linear-gradient(160deg,#4f6e2c,#d4732c 55%,#7a5a3a)}
.comment-label{left:38px;top:576px;font-size:10.5px;color:#666;letter-spacing:.3px}
.footer{left:0;top:718px;width:535px;height:34px;background:linear-gradient(180deg,#e3cfa9,#d2b88c)}
.footer .pill{position:absolute;left:38px;top:6px;font-size:6.5px;text-transform:none;font-weight:600}
.page-tab{position:absolute;left:470px;top:4px;width:24px;height:36px;background:var(--yellow);border-radius:0 0 4px 4px;display:flex;justify-content:center;padding-top:4px}
.page-num{width:18px;height:18px;border-radius:50%;background:var(--teal);color:#fff;font-size:10px;display:flex;align-items:center;justify-content:center}
</style>
</head>
<body>

<section class="page page--one">
  <div class="abs brand-tab"><span class="brand-name">VITALMERE</span></div>
  <h1 class="abs doc-title">NUTRITIONAL THERAPY<br>CONSULTATION REPORT</h1>

  <div class="abs field" style="left:38px;top:151px">Nutritionist’s name:</div>
  <div class="abs field" style="left:277px;top:151px">Client’s name:</div>
  <div class="abs field" style="left:38px;top:175px">Store location:</div>
  <div class="abs field" style="left:277px;top:175px">Date of birth:</div>
  <div class="abs field" style="left:38px;top:199px">Consultation date:</div>
  <div class="abs field" style="left:277px;top:199px">Current energy rating out of 10:</div>

  <div class="abs pill pill--grey" style="left:38px;top:243px">General comments on your food diary</div>
  <div class="abs notes ruled" style="top:262px"></div>

  <div class="abs pill pill--teal" style="left:38px;top:375px">Food / drink to have more of</div>
  <div class="abs icon" style="top:367px">
    <svg width="30" height="30" viewBox="0 0 30 30" fill="none" stroke="var(--yellow)" stroke-width="1.6"><path d="M15 10c-3-2-8-1-8 5 0 5 3 9 5 9 1.5 0 2-.8 3-.8s1.5.8 3 .8c2 0 5-4 5-9 0-6-5-7-8-5z"/><path d="M15 10c0-2 1-4 3-5"/></svg>
  </div>
  <div class="abs table" style="top:404px">
    <div class="col"><div class="col-head col-head--single">Food / drink</div><div class="col-body ruled"></div></div>
    <div class="col"><div class="col-head col-head--single">Reason</div><div class="col-body ruled"></div></div>
    <div class="col"><div class="col-head">How often should I have this food / drink?</div><div class="col-body ruled"></div></div>
  </div>

  <div class="abs pill pill--teal" style="left:38px;top:538px">Food / drink to have less of</div>
  <div class="abs icon" style="top:531px">
    <svg width="30" height="30" viewBox="0 0 30 30" fill="none" stroke="var(--yellow)" stroke-width="1.6"><path d="M15 23l-7-7c-3-3-1-8 3-8 2 0 3 1 4 2 1-1 2-2 4-2 4 0 6 5 3 8z"/><circle cx="22" cy="22" r="4.5" fill="#fff" stroke="none"/><path d="M19.8 22l1.5 1.5 2.7-3" stroke="var(--teal)"/></svg>
  </div>
  <div class="abs table" style="top:567px">
    <div class="col"><div class="col-head col-head--single">Food / drink</div><div class="col-body ruled"></div></div>
    <div class="col"><div class="col-head col-head--single">Reason</div><div class="col-body ruled"></div></div>
    <div class="col"><div class="col-head">How often can I have this food / drink?</div><div class="col-body ruled"></div></div>
  </div>

  <footer class="abs footer">
    <div class="pill pill--teal">Nutritional Therapy Consultation Report</div>
    <div class="page-tab"><span class="page-num">1</span></div>
  </footer>
</section>

<section class="page page--two">
  <div class="abs photo photo--nuts" role="img" aria-label="Photo of walnuts and nut shells on a wooden table"></div>
  <div class="abs photo photo--asparagus" role="img" aria-label="Photo of bundled green asparagus in a bowl"></div>
  <div class="abs photo photo--carrots" role="img" aria-label="Photo of fresh carrots, herbs and olive oil"></div>

  <div class="abs pill pill--grey" style="left:38px;top:145px">Food preparation advice:</div>
  <div class="abs notes ruled" style="top:164px"></div>

  <div class="abs pill pill--teal" style="left:38px;top:277px">Supplement plan</div>
  <div class="abs icon" style="top:269px">
    <svg width="30" height="30" viewBox="0 0 30 30" fill="none" stroke="var(--yellow)" stroke-width="1.6"><path d="M15 10c-3-2-8-1-8 5 0 5 3 9 5 9 1.5 0 2-.8 3-.8s1.5.8 3 .8c2 0 5-4 5-9 0-6-5-7-8-5z"/><path d="M15 10c0-2 1-4 3-5"/></svg>
  </div>
  <div class="abs table" style="top:306px">
    <div class="col"><div class="col-head col-head--single">Supplement</div><div class="col-body ruled"></div></div>
    <div class="col"><div class="col-head col-head--single">Brand</div><div class="col-body ruled"></div></div>
    <div class="col"><div class="col-head col-head--single">Dosage</div><div class="col-body ruled"></div></div>
    <div class="col"><div class="col-head col-head--single">When to take</div><div class="col-body ruled"></div></div>
  </div>

  <div class="abs pill pill--teal pill--accent" style="left:38px;top:441px">Suggested lifestyle changes:</div>
  <div class="abs icon" style="top:437px">
    <svg width="30" height="30" viewBox="0 0 30 30" fill="none" stroke="var(--yellow)" stroke-width="1.8"><path d="M8 14a7 7 0 0 1 12-5l1 1"/><path d="M21 6v4h-4"/><path d="M22 16a7 7 0 0 1-12 5l-1-1"/><path d="M9 24v-4h4"/></svg>
  </div>
  <div class="abs notes ruled" style="top:460px"></div>

  <p class="abs comment-label">PERSONAL MESSAGE / ANY OTHER COMMENTS:</p>
  <div class="abs icon" style="top:567px">
    <svg width="30" height="30" viewBox="0 0 30 30" fill="none" stroke="var(--yellow)" stroke-width="1.8"><path d="M10 19l10-11 2.5 2.5-10 11-3.5 1z"/><path d="M7 25c4-2 8 1 15-1"/></svg>
  </div>
  <div class="abs notes ruled--teal" style="top:590px"></div>

  <footer class="abs footer">
    <div class="pill pill--teal">Nutritional Therapy Consultation Report</div>
    <div class="page-tab"><span class="page-num">2</span></div>
  </footer>
</section>

</body>
</html>
```